Sign Shop website

We need a web design for a sign company called Quillby Signs that builds signs for shops such as A Frames, Banners, Tennet Boards, Shop front windows etc...

The existing site is avaliable at www.quillbysigns.com.au

We will need to have a fresh makeover. The new site must have the following:

Photo Galleries (broken down into sections)
Store Locations (currently there are 4 stores)
Online quote form
List of services
About Us Page

We just need to front page designed in photoshop (the inner page is not necessary) We have a team that can code the site up.

The website should have the exact logo. Any person who alters the logo, design will be elimated.

No Twitter, RSS, LinkedIn icons

The main colours are yellow, black, blue, red

Target Market(s)

Any business

Industry/Entity Type

It Company

Requirements
Must have
• jQuery slider banner
Should not have
• Alter the logo in any way

```html
<!DOCTYPE html>
<html lang="en">
<head>
<meta charset="utf-8">
<title>Quillby Signs &amp; Digital Printing</title>
<link rel="stylesheet" href="https://fonts.googleapis.com/css2?family=Archivo+Black&family=Oswald:wght@400;500;600&family=Crimson+Text:ital,wght@1,600;1,700&family=Arimo:wght@400;700&display=swap">
<style>
:root{
  --yellow:#f2b21c;
  --yellow-light:#fbd96a;
  --gold:#e3ab12;
  --ink:#2b2b2b;
  --olive:#4a3b12;
  --text:#4a4a4a;
  --purple:#5b2c83;
  --red:#e4261c;
  --red-dark:#b8160f;
  --green:#0c8a3a;
  --tick:#8cbc2c;
  --grey-bg:#e6e6e6;
  --footer:#d3d3d3;
  --pink:#c63f78;
  --white:#fff;
}
*{box-sizing:border-box;margin:0;padding:0}
html,body{width:845px;height:1200px;overflow:hidden;background:var(--white)}
body{font-family:"Arimo",Arial,sans-serif;color:var(--text);position:relative}
.abs{position:absolute}

/* hero */
.hero{position:absolute;left:0;top:0;width:845px;height:418px;
  background:radial-gradient(ellipse at 50% 15%,var(--yellow-light) 0%,var(--yellow) 55%,#eaa012 100%);overflow:hidden}
.hero__ground{position:absolute;left:0;top:318px;width:845px;height:100px;
  background:linear-gradient(#bdbdbd,#e9e9e9 60%,#f1f1f1)}
.topstrip{position:absolute;left:0;top:0;width:845px;height:3px;
  background:linear-gradient(90deg,var(--red) 0 16%,#1a1a1a 16% 32%,#23a8d8 32% 48%,var(--purple) 48% 64%,var(--red) 64% 80%,#23a8d8 80% 100%)}
.nav{position:absolute;top:16px;left:0;width:845px;height:40px}
.nav__item{position:absolute;top:0;text-align:center;font:500 11px "Arimo",Arial,sans-serif;color:var(--white);letter-spacing:.2px;white-space:nowrap}
.nav__item svg{display:block;margin:0 auto 8px}
.nav__item--active{color:var(--red)}
.logo{position:absolute;left:312px;top:34px;width:225px;height:60px;display:flex;align-items:center;justify-content:center;gap:8px}
.logo__mark{width:16px;height:16px;background:var(--purple)}
.logo__name{font:600 28px "Oswald",sans-serif;color:var(--purple);white-space:nowrap}
.hero__title{position:absolute;left:98px;top:128px;font:26px "Archivo Black",sans-serif;color:var(--olive);letter-spacing:.5px;z-index:2}
.hero__tagline{position:absolute;left:100px;top:167px;font:italic 700 15.5px/19px "Crimson Text",serif;color:var(--ink);white-space:nowrap;z-index:2}
.hero__billboard{position:absolute;left:100px;top:218px;width:150px;height:192px;
  background:linear-gradient(#7d7d7d,#b4b4b4);clip-path:polygon(0 18%,100% 0,100% 100%,0 100%);opacity:.85}
.hero__car{position:absolute;left:335px;top:140px;width:392px;height:268px;
  clip-path:polygon(0 55%,8% 40%,20% 22%,32% 6%,48% 0,78% 2%,90% 28%,100% 52%,100% 100%,0 100%);
  background:linear-gradient(160deg,#9fc3d8,#6f93ab 60%,#3b4d5a)}
.badge{position:absolute;left:658px;top:104px;width:54px;height:54px;border-radius:50%;background:var(--white);
  box-shadow:0 2px 4px rgba(0,0,0,.25);font:700 8px/10px "Arimo",Arial,sans-serif;color:var(--ink);text-align:center;padding-top:17px;z-index:2}
.arrow{position:absolute;top:200px}

/* locator */
.locator{position:absolute;left:0;top:418px;width:845px;height:276px;background:linear-gradient(#f6f6f6,var(--grey-bg))}
.h2{font:500 20px "Oswald",sans-serif;color:var(--ink)}
.locator__title{position:absolute;left:98px;top:30px}
.map{position:absolute;left:98px;top:66px;width:166px;height:139px;border:4px solid var(--white);outline:1px solid #bbb;
  background:linear-gradient(135deg,#e4e0d4,#d5d0c0)}
.address{position:absolute;left:276px;top:70px;font-size:11.5px;line-height:16px;color:var(--text)}
.address dt{margin-top:8px}
.address dd{font:700 16px/19px "Arimo",Arial,sans-serif;color:var(--ink)}
.address dd .code{color:var(--green)}
.address dd.street{font:400 11.5px/16px "Arimo",Arial,sans-serif;color:var(--text)}
.btn{position:absolute;display:flex;align-items:center;justify-content:center;flex-direction:column;
  background:linear-gradient(var(--red),var(--red-dark));border:2px solid #f06a5b;border-radius:5px;color:var(--white);
  font:500 19px/20px "Oswald",sans-serif;text-transform:uppercase}
.btn small{font-size:12px;line-height:13px}
.btn--find{left:109px;top:226px;width:144px;height:35px}
.btn--gallery{left:512px;top:213px;width:163px;height:48px}
.gallery{position:absolute;left:445px;top:26px;width:300px;height:182px;transform:rotate(-3deg);
  background:linear-gradient(120deg,#c9c9c9,#f7f7f7 40%,#d8e3ee);border:5px solid var(--white);box-shadow:0 3px 8px rgba(0,0,0,.25)}
.gallery__arrow{position:absolute;left:474px;top:185px}

/* welcome */
.welcome{position:absolute;left:98px;top:716px;width:428px}
.welcome__pre{font:400 19px/22px "Oswald",sans-serif;color:var(--ink)}
.welcome__title{font:500 23px/26px "Oswald",sans-serif;color:var(--purple)}
.welcome__body{margin-top:8px;font-size:9.8px;line-height:14.7px;color:var(--text)}
.readmore{position:absolute;left:456px;top:870px;width:68px;height:18px;border-radius:9px;background:var(--white);
  box-shadow:0 1px 3px rgba(0,0,0,.3);font-size:8.5px;color:var(--red);display:flex;align-items:center;justify-content:center;gap:5px}
.readmore i{width:7px;height:6px;background:var(--red);display:block;clip-path:polygon(0 0,70% 0,100% 50%,70% 100%,0 100%)}
.services{position:absolute;left:98px;top:904px}
.services__list{list-style:none;margin-top:4px;display:grid;grid-template-columns:206px 200px;row-gap:6px}
.services__list li{font-size:11px;line-height:14px;color:var(--text);display:flex;align-items:center;gap:8px}

/* quote */
.quote{position:absolute;left:560px;top:720px;width:186px;height:272px}
.quote__head{position:absolute;left:0;top:0;width:186px;height:44px;background:var(--purple);
  clip-path:polygon(0 0,100% 8%,100% 100%,3% 100%);color:var(--white);font:500 17px "Oswald",sans-serif;padding:7px 0 0 10px}
.quote__body{position:absolute;left:5px;top:42px;width:181px;height:196px;background:var(--gold);padding:12px 13px 0}
.field{display:block;width:155px;height:26px;background:var(--white);font-size:10px;color:#666;padding:8px 6px;margin-bottom:9px}
.field--msg{height:65px}
.quote__submit{position:absolute;left:5px;top:236px;width:181px;height:36px;background:linear-gradient(var(--red),var(--red-dark));
  color:var(--white);font:500 19px "Oswald",sans-serif;text-align:center;line-height:36px}

/* footer */
.footer{position:absolute;left:0;top:1062px;width:845px;height:138px;background:var(--footer)}
.footer__logo{position:absolute;left:340px;top:1042px;width:176px;height:48px;display:flex;align-items:center;justify-content:center;gap:6px}
.footer__logo .logo__name{font-size:20px}
.footer__logo .logo__mark{width:12px;height:12px}
.footer__city{position:absolute;left:98px;top:32px;font:500 16px "Oswald",sans-serif;color:var(--pink)}
.contact{position:absolute;top:58px;display:flex;gap:10px;align-items:flex-start;font-size:9px;line-height:14px;color:#555}
.contact strong{font:400 14px "Arimo",Arial,sans-serif;color:var(--ink)}
.contact strong.red{color:var(--red);font-weight:700}
.footer__badge{position:absolute;left:641px;top:58px;width:105px;height:37px;background:linear-gradient(#efefef,#cfcfcf);border:1px solid #bbb}
.footer__rule{position:absolute;left:98px;top:106px;width:648px;height:1px;background:#bdbdbd}
.footer__links{position:absolute;left:98px;top:116px;font-size:9px;color:#444;list-style:none;display:flex}
.footer__links li+li{border-left:1px solid #999;margin-left:6px;padding-left:6px}
.footer__copy{position:absolute;right:99px;top:116px;font-size:9px;color:#444}
</style>
</head>
<body>

<header class="hero">
  <div class="topstrip"></div>
  <div class="hero__ground"></div>
  <nav class="nav">
    <a class="nav__item nav__item--active" style="left:98px;width:32px">
      <svg width="14" height="13" viewBox="0 0 14 13"><path d="M7 0L0 6h2v7h4V9h2v4h4V6h2z" fill="#e4261c"/></svg>HOME</a>
    <a class="nav__item" style="left:155px;width:36px">
      <svg width="15" height="13" viewBox="0 0 15 13"><rect x="0" y="3" width="15" height="10" rx="1" fill="#1a1a1a"/><rect x="5" y="0" width="5" height="4" fill="none" stroke="#1a1a1a" stroke-width="1.5"/></svg>ABOUT</a>
    <a class="nav__item" style="left:216px;width:52px">
      <svg width="14" height="14" viewBox="0 0 14 14"><circle cx="7" cy="7" r="5" fill="#1a1a1a"/><circle cx="7" cy="7" r="2" fill="#f2b21c"/><path d="M6 0h2v14H6zM0 6h14v2H0z" fill="#1a1a1a"/></svg>SERVICES</a>
    <a class="nav__item" style="left:572px;width:86px">
      <svg width="16" height="14" viewBox="0 0 16 14"><rect x="1" y="1" width="12" height="10" fill="none" stroke="#1a1a1a" stroke-width="1.6"/><rect x="4" y="4" width="11" height="9" fill="none" stroke="#1a1a1a" stroke-width="1.6"/></svg>OUR PORTFOLIO</a>
    <a class="nav__item" style="left:682px;width:66px">
      <svg width="10" height="15" viewBox="0 0 10 15"><rect x="1" y="1" width="8" height="13" rx="1.5" fill="none" stroke="#1a1a1a" stroke-width="1.6"/><circle cx="5" cy="11.5" r="1" fill="#1a1a1a"/></svg>CONTACT US</a>
  </nav>
  <div class="logo"><span class="logo__mark"></span><span class="logo__name">Quillby Signs</span></div>

  <div class="hero__billboard" role="img" aria-label="Illustrated billboard on a post in front of a grey city skyline"></div>
  <div class="hero__car" role="img" aria-label="Small city car wrapped in printed vehicle signage"></div>

  <h1 class="hero__title">SIGN SOLUTIONS</h1>
  <p class="hero__tagline">Quillby Signs will exceed customer exectations bt<br>offering a personalised approch to clients.</p>
  <div class="badge">VEHICLE<br>SIGNAGE</div>

  <svg class="arrow" style="left:26px" width="22" height="64" viewBox="0 0 22 64"><path d="M19 2L4 32l15 30" fill="none" stroke="#fff" stroke-width="3"/></svg>
  <svg class="arrow" style="left:800px" width="22" height="64" viewBox="0 0 22 64"><path d="M3 2l15 30L3 62" fill="none" stroke="#fff" stroke-width="3"/></svg>
  <svg class="abs" style="left:0;top:410px" width="845" height="8" viewBox="0 0 845 8" preserveAspectRatio="none">
    <defs><pattern id="scallop" width="6" height="8" patternUnits="userSpaceOnUse"><path d="M0 8V4Q3 0 6 4V8z" fill="#f6f6f6"/></pattern></defs>
    <rect width="845" height="8" fill="url(#scallop)"/>
  </svg>
</header>

<section class="locator">
  <h2 class="h2 locator__title">Store Location</h2>
  <div class="map" role="img" aria-label="Street map with a pink pin marking the store"></div>
  <dl class="address">
    <dd class="street">Unit 7, 12-18 Marlow Avenue<br>Brookvale, WA 6150</dd>
    <dt>Call:</dt>
    <dd><span class="code">(08)</span> 9100 4827</dd>
    <dt>Fax:</dt>
    <dd><span class="code">(08)</span> 9100 4827</dd>
  </dl>
  <a class="btn btn--find">Find us here</a>
  <div class="gallery" role="img" aria-label="Fanned instant photos of finished signs and sign installers"></div>
  <svg class="gallery__arrow" width="24" height="50" viewBox="0 0 24 50"><path d="M6 2C0 18 2 38 20 44" fill="none" stroke="#555" stroke-width="1.3"/><path d="M14 39l7 5-8 3" fill="none" stroke="#555" stroke-width="1.3"/></svg>
  <a class="btn btn--gallery"><small>Go to</small>Photo Gallery</a>
</section>

<section class="welcome">
  <p class="welcome__pre">Welcome to</p>
  <h2 class="welcome__title">Quillby Signs &amp; Digital Printing</h2>
  <p class="welcome__body">Lorem Ipsum is simply dummy text of the printing and typesetting industry. Lorem Ipsum has been the industry's standard dummy text ever since the 1500s, when an unknown printer took a galley of type and scrambled it to make a type specimen book. It has survived not only five centuries, but also the leap into electronic typesetting, remaining essentially unchanged. It was popularised in the 1960s with the release of Letraset sheets containing Lorem Ipsum passages, and more recently with desktop publishing software like Aldus PageMaker including versions.</p>
</section>
<a class="readmore">Read More <i></i></a>

<section class="services">
  <h2 class="h2">Our Services</h2>
  <ul class="services__list">
    <li><svg width="10" height="9" viewBox="0 0 10 9"><path d="M1 5l3 3 5-7" fill="none" stroke="#8cbc2c" stroke-width="2"/></svg>Quality Stickers &amp; Decals</li>
    <li><svg width="10" height="9" viewBox="0 0 10 9"><path d="M1 5l3 3 5-7" fill="none" stroke="#8cbc2c" stroke-width="2"/></svg>Magnets</li>
    <li><svg width="10" height="9" viewBox="0 0 10 9"><path d="M1 5l3 3 5-7" fill="none" stroke="#8cbc2c" stroke-width="2"/></svg>All Sign Types</li>
    <li><svg width="10" height="9" viewBox="0 0 10 9"><path d="M1 5l3 3 5-7" fill="none" stroke="#8cbc2c" stroke-width="2"/></svg>Construction and safety Signs</li>
    <li><svg width="10" height="9" viewBox="0 0 10 9"><path d="M1 5l3 3 5-7" fill="none" stroke="#8cbc2c" stroke-width="2"/></svg>Vehicle Signage</li>
    <li><svg width="10" height="9" viewBox="0 0 10 9"><path d="M1 5l3 3 5-7" fill="none" stroke="#8cbc2c" stroke-width="2"/></svg>Window Signage</li>
  </ul>
</section>

<aside class="quote">
  <div class="quote__head">Request a Quote
    <svg class="abs" style="left:145px;top:13px" width="26" height="18" viewBox="0 0 26 18"><ellipse cx="10" cy="8" rx="9" ry="6" fill="#a7d24a"/><ellipse cx="17" cy="11" rx="8" ry="5.5" fill="#e06bb0"/></svg>
  </div>
  <div class="quote__body">
    <span class="field">Your name</span>
    <span class="field">Your email</span>
    <span class="field">Phone</span>
    <span class="field field--msg">Your massage</span>
  </div>
  <div class="quote__submit">SUBMIT NOW!</div>
</aside>

<footer class="footer">
  <h3 class="footer__city">Harbourside</h3>
  <div class="contact" style="left:100px">
    <svg width="14" height="20" viewBox="0 0 14 20"><path d="M7 0a7 7 0 0 0-7 7c0 5 7 13 7 13s7-8 7-13a7 7 0 0 0-7-7z" fill="#777"/><circle cx="7" cy="7" r="2.6" fill="#d3d3d3"/></svg>
    <span>Shop 4, 28 Tern Promenade,<br>Harbourside, W.A</span>
  </div>
  <div class="contact" style="left:268px">
    <svg width="24" height="16" viewBox="0 0 24 16"><rect width="24" height="16" rx="2" fill="#777"/><path d="M1 1l11 8 11-8" fill="none" stroke="#d3d3d3" stroke-width="1.5"/></svg>
    <span>Send us Mail at<br><strong>hello@quillbysigns.com.au</strong></span>
  </div>
  <div class="contact" style="left:488px">
    <svg width="10" height="20" viewBox="0 0 10 20"><path d="M3 0h4v5H5c-1 3-1 7 0 10h2v5H3C-1 14-1 6 3 0z" fill="#777"/></svg>
    <span>Give us a call at<br><strong class="red">08 6300 5517</strong></span>
  </div>
  <div class="footer__badge"></div>
  <div class="footer__rule"></div>
  <ul class="footer__links"><li>Home</li><li>About</li><li>Services</li><li>Our Portfolio</li><li>Contact us</li></ul>
  <p class="footer__copy">Copyright© 2013 Quillby Signs &amp; Digital Printing . All Rights Reserved.</p>
</footer>
<div class="footer__logo"><span class="logo__mark"></span><span class="logo__name">Quillby Signs</span></div>

</body>
</html>
```